Tervolan Pty Ltd professional business card

A professional business card template using the colours from the supplied logo.
Clean crisp lines while, Modern while not being over the top.

Target Market(s)

Construction, commerical and industrial

Industry/Entity Type

Communications

Contact Information for Business Card

For a Communications, IT, Optical fibre installation company

Colors
37b8a4

```html
<!DOCTYPE html>
<html lang="en">
<head>
<meta charset="utf-8">
<title>Tervolan Pty Ltd – Business Card</title>
<link rel="stylesheet" href="https://fonts.googleapis.com/css2?family=Lato:wght@400;700;900&display=swap">
<style>
  :root {
    --stage: #1f1f21;
    --card-front: #ffffff;
    --card-back: #48484c;
    --card-back-deep: #404044;
    --teal: #1e97a0;
    --teal-light: #6fb9c0;
    --grey-text: #5f6063;
    --mark-grey: #6a6a6e;
  }
  * { margin: 0; padding: 0; box-sizing: border-box; }
  html, body {
    width: 1200px; height: 1108px; overflow: hidden;
    background: var(--stage);
    font-family: "Lato", sans-serif;
  }
  .stage {
    position: relative; width: 1200px; height: 1108px;
  }
  .card {
    position: absolute; top: 214px;
    width: 390px; height: 680px;
    border-radius: 22px;
    overflow: hidden;
  }
  .card--front { left: 170px; background: var(--card-front); text-align: center; }
  .card--back { left: 640px; background: var(--card-back); }

  .brand {
    position: absolute; top: 118px; left: 0; right: 0;
    display: flex; align-items: center; justify-content: center; gap: 14px;
  }
  .brand__dot { width: 22px; height: 22px; border-radius: 50%; background: var(--teal); }
  .brand__name {
    font-size: 62px; font-weight: 700; color: var(--mark-grey);
    letter-spacing: 1px;
  }

  .person { position: absolute; top: 340px; left: 0; right: 0; }
  .person__name {
    font-size: 40px; font-weight: 900; color: var(--teal);
    text-transform: uppercase; letter-spacing: 0.5px;
  }
  .person__role { font-size: 23px; color: var(--grey-text); margin-top: 2px; }

  .divider-icons {
    position: absolute; top: 446px; left: 50px; right: 50px;
    display: flex; align-items: center; gap: 8px;
  }
  .divider-icons .rule { flex: 1; height: 1px; background: var(--teal-light); }
  .icon { width: 28px; height: 28px; }

  .contact { position: absolute; top: 488px; left: 0; right: 0; }
  .contact p { font-size: 23px; line-height: 31px; color: var(--grey-text); }

  .rule-plain {
    position: absolute; top: 592px; left: 80px; right: 80px;
    height: 1px; background: var(--teal-light);
  }
  .address { position: absolute; top: 606px; left: 0; right: 0; }
  .address p { font-size: 22px; line-height: 30px; color: var(--grey-text); }

  .back-pattern {
    position: absolute; inset: 0;
    background: linear-gradient(180deg, #55555a 0%, var(--card-back) 55%, var(--card-back-deep) 100%);
  }
  .back-brand {
    position: absolute; right: 44px; bottom: 110px;
    display: flex; align-items: center; gap: 10px;
  }
  .back-brand__dot { width: 16px; height: 16px; border-radius: 50%; background: var(--teal); }
  .back-brand__name { font-size: 30px; font-weight: 700; color: #ffffff; }
</style>
</head>
<body>
<main class="stage">
  <section class="card card--front" aria-label="Business card front">
    <div class="brand">
      <span class="brand__dot"></span>
      <span class="brand__name">Tervolan</span>
    </div>

    <div class="person">
      <h1 class="person__name">Daniel Hart</h1>
      <p class="person__role">Managing Director</p>
    </div>

    <div class="divider-icons">
      <span class="rule"></span>
      <svg class="icon" viewBox="0 0 28 28" aria-label="Phone" role="img">
        <circle cx="14" cy="14" r="13" fill="var(--teal)"/>
        <path d="M9.5 8.5c1-1 2-.8 2.5 0l1 1.8c.4.7.2 1.3-.4 1.8l-.7.6c.6 1.5 1.8 2.7 3.3 3.3l.6-.7c.5-.6 1.1-.8 1.8-.4l1.8 1c.8.5 1 1.5 0 2.5-1.2 1.2-3 1.4-5.5-.4-2.3-1.7-4-3.4-5.1-5.6-1-2-.6-3.6.7-3.9z" fill="#fff"/>
      </svg>
      <svg class="icon" viewBox="0 0 28 28" aria-label="Email" role="img">
        <circle cx="14" cy="14" r="13" fill="var(--teal)"/>
        <rect x="7.5" y="9.5" width="13" height="9" fill="none" stroke="#fff" stroke-width="1.6"/>
        <path d="M7.5 9.5l6.5 5 6.5-5" fill="none" stroke="#fff" stroke-width="1.6"/>
      </svg>
      <svg class="icon" viewBox="0 0 28 28" aria-label="Website" role="img">
        <circle cx="14" cy="14" r="13" fill="var(--teal)"/>
        <circle cx="14" cy="14" r="6.5" fill="none" stroke="#fff" stroke-width="1.4"/>
        <ellipse cx="14" cy="14" rx="2.8" ry="6.5" fill="none" stroke="#fff" stroke-width="1.2"/>
        <path d="M7.5 14h13M8.5 11h11M8.5 17h11" stroke="#fff" stroke-width="1.1"/>
      </svg>
      <span class="rule"></span>
    </div>

    <div class="contact">
      <p>04815-27390</p>
      <p>daniel@tervolan.com</p>
      <p>www.tervolan.com</p>
    </div>

    <div class="rule-plain"></div>

    <div class="address">
      <p>1234 First Line Address</p>
      <p>5678 Second Line Address</p>
    </div>
  </section>

  <section class="card card--back" aria-label="Business card back">
    <div class="back-pattern" role="img" aria-label="Faint repeating brand decoration across the dark grey back"></div>
    <div class="back-brand">
      <span class="back-brand__dot"></span>
      <span class="back-brand__name">Tervolan</span>
    </div>
  </section>
</main>
</body>
</html>
```